Tallwick Haven National Website

We need a website to match our Logo. We will be selling american made vapeing Oils, batteries, Cartomizers, Clearomizers. We have a wharehouse location with couches, TVs streaming clipora, vending machine, and the worlds first flavor mixing bar. We have the lowest priced high grade oils. We will send pictures of the location. Relaxed atmoshpere and no lines for purchase. VIP cards for regulars.

(PLEASE KNOW THAT THE LOGO IS THE UPPER RIGHT LOGO ONLY OF THE FOUR ON THE FILE I ATTACHED)
Updates

Keep in mind we are are only looking for concept and a non coded website

Please know that we are looking for a non coded website

Industry/Entity Type

Purchase

Requirements
Must have
• Online cart, Blog,

```html
<!DOCTYPE html>
<html lang="en">
<head>
<meta charset="utf-8">
<title>Tallwick Haven</title>
<link href="https://fonts.googleapis.com/css2?family=Open+Sans:ital,wght@0,400;0,600;0,700;0,800;1,400&family=Oswald:wght@500;600&family=Lora:ital@1&display=swap" rel="stylesheet">
<style>
:root{
  --ink:#222;
  --muted:#8a8a8a;
  --line:#d8d8d8;
  --green:#7dbb1f;
  --green-dark:#5f9412;
  --red:#c8202a;
  --dark:#1c1c1c;
  --darker:#121212;
  --panel:#262626;
  --white:#fff;
}
*{box-sizing:border-box;margin:0;padding:0}
html,body{width:1200px;height:2727px;overflow:hidden}
body{background:var(--white);font-family:"Open Sans",Arial,sans-serif;color:var(--ink);position:relative}

/* hero */
.hero{position:absolute;left:0;top:0;width:1200px;height:600px;
  background:radial-gradient(ellipse at 70% 40%,#c8b8a6 0%,#7a6a5c 35%,#3a3230 70%,#1c1a1a 100%)}
.header{position:absolute;left:0;top:0;width:1200px;height:95px;background:rgba(0,0,0,.72)}
.logo{position:absolute;left:128px;top:12px;font-size:28px;font-weight:700;color:var(--white);letter-spacing:-.5px}
.topbar{position:absolute;right:128px;top:8px;font-size:11px;color:#ddd;display:flex;gap:30px}
.topbar b{color:var(--white)}
.topbar .cart-count{color:var(--green)}
.nav{position:absolute;left:128px;top:60px;display:flex;gap:26px;font-size:13px;color:var(--white);font-weight:600}
.webstore{position:absolute;left:440px;top:50px;width:112px;height:34px;border-radius:17px;border:1px solid #444;background:#111;color:var(--green);font-weight:700;font-size:15px;text-align:center;line-height:32px}
.browse{position:absolute;left:575px;top:60px;font-size:13px;color:#ddd}
.browse b{color:var(--white);font-weight:600}
.search{position:absolute;left:878px;top:54px;width:218px;height:28px;background:#0c0c0c;border:1px solid #555;color:#ccc;font-size:12px;padding:5px 10px}
.search svg{position:absolute;right:8px;top:6px}
.hero-title{position:absolute;left:128px;top:380px;background:rgba(25,25,25,.85);color:var(--white);font-size:41px;font-weight:800;padding:2px 14px 4px}
.hero-sub{position:absolute;left:128px;top:442px;background:rgba(25,25,25,.85);color:var(--white);font-size:21px;font-weight:700;padding:6px 14px}
.arrows{position:absolute;left:128px;top:512px;display:flex;gap:10px}
.arrows span{width:34px;height:34px;background:var(--green);display:flex;align-items:center;justify-content:center}
.thumbs{position:absolute;left:0;top:600px;width:1200px;height:150px;background:var(--dark)}
.thumbs .row{position:absolute;left:128px;top:18px;display:flex;gap:22px}
.thumb{width:218px;height:102px;background:linear-gradient(135deg,#5a4e46,#2e2a28);border:3px solid #111}
.thumb.active{border-color:var(--green)}

/* sections */
.sec-title{position:absolute;left:128px;width:944px;height:34px;display:flex;align-items:center;gap:20px;font-family:"Oswald",sans-serif;font-weight:600;font-size:24px;line-height:34px;color:var(--ink)}
.sec-title::before,.sec-title::after{content:"";flex:1;height:1px;background:var(--line)}
.products{position:absolute;left:128px;display:flex;gap:16px}
.product{width:224px}
.product .pic{height:160px;border:1px solid var(--line);background:linear-gradient(160deg,#e9e9e9,#9a9a9a)}
.product .pic.mint{background:linear-gradient(160deg,#5aa044,#2e6b22)}
.product .pic.jar{background:linear-gradient(160deg,#f1f1f1,#c24a3a 160%)}
.product .pic.lamp{background:linear-gradient(160deg,#fafafa,#d4b8a4)}
.product .meta{display:flex;justify-content:space-between;align-items:center;margin-top:14px;font-size:12px}
.product .price{font-weight:700;font-size:12px}
.product .price s{color:var(--red);font-weight:400;margin-right:4px}
.stars{color:var(--red);font-size:13px;letter-spacing:1px;margin-top:2px}
.add{display:inline-block;margin-top:10px;background:var(--red);color:var(--white);font-size:9px;font-weight:700;padding:4px 8px}

.vip{position:absolute;left:128px;top:1152px;width:944px;height:104px;border:1px solid var(--line);box-shadow:0 1px 4px rgba(0,0,0,.08)}
.vip h3{position:absolute;left:30px;top:30px;font-size:20px;font-weight:700}
.vip p{position:absolute;left:30px;top:62px;font-size:11px;color:var(--muted)}
.vip .btn{position:absolute;right:30px;top:31px;width:220px;height:42px;border-radius:21px;background:linear-gradient(#9fd548,var(--green-dark));color:var(--white);font-size:15px;font-weight:600;text-align:center;line-height:42px}

.to-store{position:absolute;left:940px;top:1946px;font-size:14px;color:var(--green);font-weight:600}
.divider{position:absolute;left:128px;top:2000px;width:944px;height:1px;background:var(--line)}

.cols{position:absolute;left:128px;top:2036px;width:944px;display:flex;gap:44px}
.col{width:285px;font-size:11px}
.col h4{font-size:13px;font-weight:700;margin-bottom:24px}
.post{display:flex;gap:14px;margin-bottom:34px}
.post .sq{width:55px;height:55px;background:#141414;flex:none}
.post p{color:#555;line-height:1.55}
.post small{display:block;color:var(--muted);font-style:italic;font-size:10px;margin-top:4px}
.tweet{margin-bottom:30px;line-height:1.6;color:#555}
.tweet b{color:var(--green);font-weight:600}
.tweet small{color:var(--muted);font-style:italic;font-size:10px}
.say .who{display:flex;gap:14px;margin-bottom:12px}
.say .who .sq{width:55px;height:55px;background:#141414}
.say .who b{display:block;font-size:12px}
.say .who span{color:var(--muted);font-size:10px}
.say q{display:block;font-family:"Lora",serif;font-style:italic;color:#666;line-height:1.6;margin-bottom:28px;quotes:none}

.footer{position:absolute;left:0;top:2468px;width:1200px;height:218px;background:var(--panel)}
.footer .brand{position:absolute;left:128px;top:26px;color:var(--white);font-size:14px;font-weight:700}
.footer .about{position:absolute;left:128px;top:54px;width:500px;color:#9a9a9a;font-size:11px;line-height:1.7}
.footer .contact{position:absolute;left:128px;top:140px;color:#bbb;font-size:11px}
.footer .contact span{margin-right:18px}
.sub{position:absolute;left:778px;top:26px;width:294px;color:#bbb;font-size:11px;line-height:1.7}
.sub h4{color:var(--white);font-size:13px;margin-bottom:6px}
.sub .form{display:flex;margin-top:16px}
.sub .field{width:200px;height:30px;background:#111;border:1px solid #444;color:#888;font-size:11px;padding:6px 10px}
.sub .go{width:80px;height:30px;margin-left:8px;background:#e8e8e8;color:#222;font-size:11px;font-weight:600;text-align:center;line-height:30px}
.bottom{position:absolute;left:0;top:2686px;width:1200px;height:41px;background:var(--darker);color:#888;font-size:11px}
.bottom .copy{position:absolute;left:128px;top:13px}
.bottom .social{position:absolute;right:128px;top:6px;display:flex;align-items:center;gap:10px;color:var(--white);font-weight:600}
.bottom .social i{width:28px;height:28px;border:2px solid #ddd;border-radius:50%;display:block}
</style>
</head>
<body>

<section class="hero" role="img" aria-label="Photo of a man exhaling vapor at a lit bar">
</section>
<header class="header">
  <div class="logo">Tallwick Haven</div>
  <div class="topbar"><span>Welcome visitor you can <b>login</b> or <b>create an account</b>.</span><span><b>Shopping Cart</b> <span class="cart-count">( 1 item - $60.00 )</span></span></div>
  <nav class="nav"><span>Home</span><span>Location</span><span>Blog</span><span>Contact</span></nav>
  <div class="webstore">Webstore</div>
  <div class="browse">Browse : <b>eLiquid Flavors</b> &#9662;</div>
  <div class="search">Search...<svg width="14" height="14" viewBox="0 0 14 14"><circle cx="6" cy="6" r="4.5" fill="none" stroke="#ccc" stroke-width="1.6"/><line x1="9.3" y1="9.3" x2="13" y2="13" stroke="#ccc" stroke-width="1.8"/></svg></div>
</header>
<h1 class="hero-title">The first Vapor Oil Flavor Mix Bar</h1>
<p class="hero-sub">Try, and exprience new flavor, mix it your own !</p>
<div class="arrows">
  <span><svg width="10" height="12" viewBox="0 0 10 12"><path d="M8 1 2 6l6 5" fill="none" stroke="#fff" stroke-width="2.4"/></svg></span>
  <span><svg width="10" height="12" viewBox="0 0 10 12"><path d="M2 1l6 5-6 5" fill="none" stroke="#fff" stroke-width="2.4"/></svg></span>
</div>
<div class="thumbs">
  <div class="row">
    <div class="thumb active" role="img" aria-label="Photo of the mixing bar"></div>
    <div class="thumb" role="img" aria-label="Photo of the lounge with TVs"></div>
    <div class="thumb" role="img" aria-label="Photo of friends on the couches"></div>
    <div class="thumb" role="img" aria-label="Photo of a customer vaping"></div>
  </div>
</div>

<h2 class="sec-title" style="top:790px">New Arrivals</h2>
<div class="products" style="top:848px">
  <div class="product"><div class="pic" role="img" aria-label="Product photo of portable vaporizers"></div><div class="meta"><span>Lumiro Portable Vaporizers</span></div><div class="meta" style="margin-top:2px"><span class="stars">★★★★★</span><span class="price">$107.75</span></div><span class="add">ADD TO CART</span></div>
  <div class="product"><div class="pic" role="img" aria-label="Product photo of a vaporizer set"></div><div class="meta"><span>Caldera Classics Set</span></div><div class="meta" style="margin-top:2px"><span class="stars">★★★★★</span><span class="price">$119.50</span></div><span class="add">ADD TO CART</span></div>
  <div class="product"><div class="pic" role="img" aria-label="Product photo of a vaporizer"></div><div class="meta"><span>Vaporo ONE Vaporizer</span></div><div class="meta" style="margin-top:2px"><span class="stars">★★★★★</span><span class="price"><s>$150.00</s>$119.50</span></div><span class="add">ADD TO CART</span></div>
  <div class="product"><div class="pic" role="img" aria-label="Product photo of a vaporizer set with box"></div><div class="meta"><span>Ample Vapor Set</span></div><div class="meta" style="margin-top:2px"><span class="stars">★★★★★</span><span class="price">$75.00</span></div><span class="add">ADD TO CART</span></div>
</div>

<div class="vip">
  <h3>Sign up now and get a free VIP Cards</h3>
  <p>Sign up for the site to get promo, updates, and a free VIP Cards as regulars on our wharehouse</p>
  <div class="btn">Sign me up</div>
</div>

<h2 class="sec-title" style="top:1272px">Top Sellers</h2>
<div class="products" style="top:1328px">
  <div class="product"><div class="pic" role="img" aria-label="Product photo of a starter kit case"></div><div class="meta"><span>Evo Tank System Starter Kit</span></div><div class="meta" style="margin-top:2px"><span class="stars">★★★★★</span><span class="price">$47.75</span></div><span class="add">ADD TO CART</span></div>
  <div class="product"><div class="pic mint" role="img" aria-label="Photo of mint leaves"></div><div class="meta"><span>Menthol eLiquid</span></div><div class="meta" style="margin-top:2px"><span class="stars">★★★★★</span><span class="price">$119.50</span></div><span class="add">ADD TO CART</span></div>
  <div class="product"><div class="pic jar" role="img" aria-label="Product photo of a jar of herb disks"></div><div class="meta"><span>Vaporo Herb Disk - 10 pack</span></div><div class="meta" style="margin-top:2px"><span class="stars">★★★★★</span><span class="price">$37.75</span></div><span class="add">ADD TO CART</span></div>
  <div class="product"><div class="pic lamp" role="img" aria-label="Product photo of a glass vaporizer"></div><div class="meta"><span>Aroma Therapy Super Vaporizer</span></div><div class="meta" style="margin-top:2px"><span class="stars">★★★★★</span><span class="price">$45.00</span></div><span class="add">ADD TO CART</span></div>
</div>
<div class="products" style="top:1650px">
  <div class="product"><div class="pic" role="img" aria-label="Product photo of a starter kit case"></div><div class="meta"><span>Evo Tank System Starter Kit</span></div><div class="meta" style="margin-top:2px"><span class="stars">★★★★★</span><span class="price">$47.75</span></div><span class="add">ADD TO CART</span></div>
  <div class="product"><div class="pic mint" role="img" aria-label="Photo of mint leaves"></div><div class="meta"><span>Menthol eLiquid</span></div><div class="meta" style="margin-top:2px"><span class="stars">★★★★★</span><span class="price">$119.50</span></div><span class="add">ADD TO CART</span></div>
  <div class="product"><div class="pic jar" role="img" aria-label="Product photo of a jar of herb disks"></div><div class="meta"><span>Vaporo Herb Disk - 10 pack</span></div><div class="meta" style="margin-top:2px"><span class="stars">★★★★★</span><span class="price">$37.75</span></div><span class="add">ADD TO CART</span></div>
  <div class="product"><div class="pic lamp" role="img" aria-label="Product photo of a glass vaporizer"></div><div class="meta"><span>Aroma Therapy Super Vaporizer</span></div><div class="meta" style="margin-top:2px"><span class="stars">★★★★★</span><span class="price">$45.00</span></div><span class="add">ADD TO CART</span></div>
</div>

<div class="to-store">go to webstore &#10230;</div>
<div class="divider"></div>

<div class="cols">
  <div class="col">
    <h4>Updates from our Blog</h4>
    <div class="post"><div class="sq"></div><p>Donec sed odio dui. Nulla vitae elit libero, a pharetra augue. Nullam id dolor<small>November 1 2012, 2 Comments</small></p></div>
    <div class="post"><div class="sq"></div><p>Donec sed odio dui. Nulla vitae elit libero, a pharetra augue. Nullam id dolor<small>November 1 2012, 2 Comments</small></p></div>
    <div class="post"><div class="sq"></div><p>Donec sed odio dui. Nulla vitae elit libero, a pharetra augue. Nullam id dolor<small>November 1 2012, 2 Comments</small></p></div>
    <div class="post"><div class="sq"></div><p>Donec sed odio dui. Nulla vitae elit libero, a pharetra augue. Nullam id dolor<small>November 1 2012, 2 Comments</small></p></div>
  </div>
  <div class="col">
    <h4>Musings in 140 characters or less.</h4>
    <p class="tweet"><b>@JonasMerrit</b> I'm almost 50 years of age and new at vaporizing, and thing thing is AWSOME!!! No complaints here at all. <small>22 minutes ago</small></p>
    <p class="tweet"><b>@JonasMerrit</b> I'm almost 50 years of age and new at vaporizing, and thing thing is AWSOME!!! No complaints here at all. <small>22 minutes ago</small></p>
    <p class="tweet"><b>@JonasMerrit</b> I'm almost 50 years of age and new at vaporizing, and thing thing is AWSOME!!! No complaints here at all. <small>22 minutes ago</small></p>
    <p class="tweet"><b>@JonasMerrit</b> I'm almost 50 years of age and new at vaporizing, and thing thing is AWSOME!!! No complaints here at all. <small>22 minutes ago</small></p>
  </div>
  <div class="col say">
    <h4>What customers are sayin'.</h4>
    <div class="who"><div class="sq"></div><div><b>Pavel Orlin</b><span>Vapor starter</span></div></div>
    <q>"Donec sed odio dui. Nulla vitae elit libero, a pharetra augue. Nullam id dolor id nibh ultricies vehicula ut id elit. Integer posuere erat a ante venenatis dapibus posuere velit aliquet."</q>
    <div class="who"><div class="sq"></div><div><b>Dara Vinsk</b><span>Vapor Critics</span></div></div>
    <q>"Donec sed odio dui. Nulla vitae elit libero, a pharetra augue. Nullam id dolor id nibh ultricies vehicula ut id elit. Integer posuere erat a ante venenatis dapibus posuere velit aliquet."</q>
  </div>
</div>

<footer class="footer">
  <div class="brand">Tallwick Haven</div>
  <p class="about">Sed ornare dictum mi, sed rutrum metus condimentum sodales. Fusce quis tellus mollis sapien porta placerat. In dapibus velit eget felis rutrum posuere. Pellentesque tincidunt augue vitae diam auctor id fermentum ante elementum. Vestibulum in luctus urna. Vivamus euismod, ligula eu commodo accumsan.</p>
  <p class="contact"><span>Email: hello@tallwickhaven.com</span><span>Tel: 1-555-014-2200</span></p>
  <div class="sub">
    <h4>Subscribe and get the inside scoop.</h4>
    Subscribe to our newsletter and get exclusive deals you wont find anywhere else straight to your inbox!
    <div class="form"><div class="field">enter your email address</div><div class="go">subscribe</div></div>
  </div>
</footer>
<div class="bottom">
  <span class="copy">Copyright 2012 • All Rights Reserved.</span>
  <div class="social">Stay Connected <i></i><i></i></div>
</div>

</body>
</html>
```